4 Poster Designs required for Nail Salon

We require 4 poster designs that will be displayed inside a shopping centre. Each design should contain our logo and the words "Located next to TallMart" (or similar). Design 1 (MOTHERS DAY) should contain the words "Mothers Day Special" and "$10 gift voucher when you spend over $50". Design 2 (CHRISTMAS) should contain the words "Christmas in July" and "Purchase a set of nails and get a $10 gift voucher". Design 3 (ALL YEAR) should contain the words "New Deluxe Spa Pedicure Service" and the words "Try our new Deluxe Spa Pedicure and get a free nail buff, shape and polish for your fingernails". Design 4 (ALL YEAR 2)should contain high quality nail salon image(s) and the words "Now Open". We like designs that support our image of high quality/fun/clean and safe.
Updates
I will close this early. In 24 hours.
Target Market(s)
Rich mums
Industry/Entity Type
Shopping
Look and feel
Each slider illustrates characteristics of the customer's brand and the style your logo design should communicate.

```html
<!DOCTYPE html>
<html lang="en">
<head>
<meta charset="utf-8">
<title>Glimmer Nail Salon – Shopping Centre Posters</title>
<link rel="stylesheet" href="https://fonts.googleapis.com/css2?family=Bebas+Neue&family=Roboto+Condensed:wght@400&family=Quicksand:wght@500;600&display=swap">
<style>
  :root {
    --plum: #5c2146;
    --plum-deep: #4a1638;
    --rose: #c2577f;
    --rose-light: #e6a9c2;
    --blush: #f4dbe6;
    --paper: #ffffff;
    --shadow: #f1c4d6;
  }
  * { box-sizing: border-box; margin: 0; padding: 0; }
  html, body { width: 848px; height: 1200px; overflow: hidden; background: var(--paper); }
  .poster-sheet {
    position: relative; width: 848px; height: 1200px;
    display: grid; grid-template-columns: 424px 424px; grid-template-rows: 600px 600px;
  }
  .poster { position: relative; width: 424px; height: 600px; background: var(--paper); }
  .poster__visual {
    position: absolute; left: 6px; top: 6px; width: 412px; height: 516px;
    overflow: hidden; border: 4px solid var(--paper); outline: 1px solid var(--rose-light);
  }
  .poster__photo { position: absolute; inset: 0; }
  .photo--roses { background: radial-gradient(ellipse at 25% 80%, #e9a7c0 0%, #f3cfdd 40%, #f8e4ec 75%); }
  .photo--beach { background: linear-gradient(180deg, #c76a93 0%, #b35582 35%, #e9b3c8 52%, #a94a77 60%, #d98bab 85%, #f1c5d6 100%); }
  .photo--spa { background: radial-gradient(ellipse at 50% 20%, #f3d2df 0%, #d889a8 45%, #b85a83 100%); }
  .photo--salon { background: linear-gradient(180deg, #d894b0 0%, #efc9d8 40%, #c06a90 60%, #e5b2c6 100%); }

  .brand {
    position: absolute; left: 50%; top: 8px; transform: translateX(-50%);
    width: 168px; height: 72px; background: var(--plum);
    display: flex; flex-direction: column; align-items: center; justify-content: center;
    color: var(--paper); font-family: "Quicksand", sans-serif;
  }
  .brand__name { font-size: 30px; font-weight: 500; letter-spacing: 1px; line-height: 1; }
  .brand__sub { font-size: 11px; font-weight: 500; margin-top: 4px; margin-left: 60px; }
  .location {
    position: absolute; left: 0; right: 0; top: 84px; text-align: center;
    font-family: "Quicksand", sans-serif; font-weight: 600; font-size: 11px; color: var(--plum-deep);
  }
  .headline {
    position: absolute; left: 0; right: 0; text-align: center;
    font-family: "Bebas Neue", sans-serif; color: var(--plum);
    text-shadow: 3px 3px 0 var(--shadow); line-height: 0.9;
  }
  .offer {
    position: absolute; left: 0; right: 0; text-align: center;
    font-family: "Bebas Neue", sans-serif; color: var(--plum);
    text-shadow: 2px 2px 0 var(--shadow); line-height: 1;
  }
  .rule { position: absolute; left: 64px; right: 64px; height: 4px; background: var(--plum); }

  .contact {
    position: absolute; left: 0; right: 0; top: 526px; height: 74px;
    font-family: "Roboto Condensed", sans-serif; font-size: 11px; color: var(--rose);
  }
  .contact__row { display: flex; justify-content: center; align-items: center; gap: 14px; height: 22px; }
  .contact__item { display: flex; align-items: center; gap: 5px; white-space: nowrap; }
  .icon { width: 18px; height: 18px; flex: none; }
</style>
</head>
<body>
<svg width="0" height="0" style="position:absolute">
  <defs>
    <symbol id="icon-home" viewBox="0 0 18 18"><circle cx="9" cy="9" r="8" fill="none" stroke="#c2577f" stroke-width="1.2"/><path d="M4.5 9 L9 5 L13.5 9 M6 8.5 V13 H12 V8.5" fill="none" stroke="#c2577f" stroke-width="1.3"/></symbol>
    <symbol id="icon-phone" viewBox="0 0 18 18"><circle cx="9" cy="9" r="8" fill="none" stroke="#c2577f" stroke-width="1.2"/><path d="M6 5 L7.5 5 L8.3 7.2 L7.3 8 Q8 10 10 10.7 L10.8 9.7 L13 10.5 L13 12 Q9 13 6 9 Q5 7 6 5 Z" fill="#c2577f"/></symbol>
    <symbol id="icon-social" viewBox="0 0 18 18"><circle cx="9" cy="9" r="8" fill="none" stroke="#c2577f" stroke-width="1.2"/></symbol>
    <symbol id="icon-mail" viewBox="0 0 18 18"><circle cx="9" cy="9" r="8" fill="none" stroke="#c2577f" stroke-width="1.2"/><rect x="4.5" y="6" width="9" height="6" fill="none" stroke="#c2577f" stroke-width="1.1"/><path d="M4.5 6 L9 9.5 L13.5 6" fill="none" stroke="#c2577f" stroke-width="1.1"/></symbol>
    <symbol id="icon-web" viewBox="0 0 18 18"><circle cx="9" cy="9" r="8" fill="none" stroke="#c2577f" stroke-width="1.2"/><circle cx="9" cy="9" r="4.5" fill="none" stroke="#c2577f" stroke-width="1"/><ellipse cx="9" cy="9" rx="2" ry="4.5" fill="none" stroke="#c2577f" stroke-width="1"/><path d="M4.5 9 H13.5" stroke="#c2577f" stroke-width="1"/></symbol>
  </defs>
</svg>

<main class="poster-sheet">

  <!-- Mothers Day -->
  <section class="poster poster--mothers-day">
    <div class="poster__visual">
      <div class="poster__photo photo--roses" role="img" aria-label="Soft pink roses, butterflies and a Happy Mothers Day card"></div>
      <div class="brand"><span class="brand__name">Glimmer</span><span class="brand__sub">Nail Salon</span></div>
      <p class="location">Located next to TallMart</p>
      <h1 class="headline" style="top:146px;font-size:64px;">Mothers Day</h1>
      <h1 class="headline" style="top:206px;font-size:118px;">Special</h1>
      <p class="offer" style="top:424px;font-size:38px;">$10 Gift Voucher</p>
      <p class="offer" style="top:460px;font-size:26px;">When you spend over $50</p>
    </div>
    <footer class="contact">
      <div class="contact__row"><span class="contact__item"><svg class="icon"><use href="#icon-home"/></svg>Shop 14 Larkfield Shopping Centre, 22-30 Marlow Avenue Larkfield, ACT 2690</span></div>
      <div class="contact__row"><span class="contact__item"><svg class="icon"><use href="#icon-phone"/></svg>(02) 5550 1842</span><span class="contact__item"><svg class="icon"><use href="#icon-social"/></svg>/glimmernailsalonstudio</span></div>
      <div class="contact__row"><span class="contact__item"><svg class="icon"><use href="#icon-mail"/></svg>hi@glimmernails.example</span><span class="contact__item"><svg class="icon"><use href="#icon-web"/></svg>www.glimmernailsalon.example</span></div>
    </footer>
  </section>

  <!-- Christmas in July -->
  <section class="poster poster--christmas">
    <div class="poster__visual">
      <div class="poster__photo photo--beach" role="img" aria-label="Sunset beach with a Santa hat and a cocktail on a towel"></div>
      <div class="brand"><span class="brand__name">Glimmer</span><span class="brand__sub">Nail Salon</span></div>
      <p class="location">Located next to TallMart</p>
      <h1 class="headline" style="top:146px;font-size:64px;">Christmas</h1>
      <h1 class="headline" style="top:206px;font-size:118px;">In July</h1>
      <p class="offer" style="top:432px;font-size:27px;">Purchase a set of nails</p>
      <p class="offer" style="top:460px;font-size:27px;">and get a $10 gift voucher</p>
    </div>
    <footer class="contact">
      <div class="contact__row"><span class="contact__item"><svg class="icon"><use href="#icon-home"/></svg>Shop 14 Larkfield Shopping Centre, 22-30 Marlow Avenue Larkfield, ACT 2690</span></div>
      <div class="contact__row"><span class="contact__item"><svg class="icon"><use href="#icon-phone"/></svg>(02) 5550 1842</span><span class="contact__item"><svg class="icon"><use href="#icon-social"/></svg>/glimmernailsalonstudio</span></div>
      <div class="contact__row"><span class="contact__item"><svg class="icon"><use href="#icon-mail"/></svg>hi@glimmernails.example</span><span class="contact__item"><svg class="icon"><use href="#icon-web"/></svg>www.glimmernailsalon.example</span></div>
    </footer>
  </section>

  <!-- Deluxe Spa Pedicure -->
  <section class="poster poster--pedicure">
    <div class="poster__visual">
      <div class="poster__photo photo--spa" role="img" aria-label="Feet in a petal-filled spa bowl, hands, flowers and a pumice sponge"></div>
      <div class="brand"><span class="brand__name">Glimmer</span><span class="brand__sub">Nail Salon</span></div>
      <p class="location">Located next to TallMart</p>
      <h1 class="headline" style="top:188px;font-size:54px;">New Deluxe Spa<br>Pedicure Service</h1>
      <p class="offer" style="top:436px;font-size:20px;">Try our new deluxe spa pedicure and get a free nail buff,</p>
      <p class="offer" style="top:458px;font-size:27px;">shape and polish for your fingernails</p>
    </div>
    <footer class="contact">
      <div class="contact__row"><span class="contact__item"><svg class="icon"><use href="#icon-home"/></svg>Shop 14 Larkfield Shopping Centre, 22-30 Marlow Avenue Larkfield, ACT 2690</span></div>
      <div class="contact__row"><span class="contact__item"><svg class="icon"><use href="#icon-phone"/></svg>(02) 5550 1842</span><span class="contact__item"><svg class="icon"><use href="#icon-social"/></svg>/glimmernailsalonstudio</span></div>
      <div class="contact__row"><span class="contact__item"><svg class="icon"><use href="#icon-mail"/></svg>hi@glimmernails.example</span><span class="contact__item"><svg class="icon"><use href="#icon-web"/></svg>www.glimmernailsalon.example</span></div>
    </footer>
  </section>

  <!-- Now Open -->
  <section class="poster poster--now-open">
    <div class="poster__visual">
      <div class="poster__photo photo--salon" role="img" aria-label="Bright salon interior with nail stations and white pedicure chairs"></div>
      <div class="brand"><span class="brand__name">Glimmer</span><span class="brand__sub">Nail Salon</span></div>
      <p class="location">Located next to TallMart</p>
      <h1 class="headline" style="top:218px;font-size:112px;">Now Open</h1>
      <div class="rule" style="top:318px;"></div>
    </div>
    <footer class="contact">
      <div class="contact__row"><span class="contact__item"><svg class="icon"><use href="#icon-home"/></svg>Shop 14 Larkfield Shopping Centre, 22-30 Marlow Avenue Larkfield, ACT 2690</span></div>
      <div class="contact__row"><span class="contact__item"><svg class="icon"><use href="#icon-phone"/></svg>(02) 5550 1842</span><span class="contact__item"><svg class="icon"><use href="#icon-social"/></svg>/glimmernailsalonstudio</span></div>
      <div class="contact__row"><span class="contact__item"><svg class="icon"><use href="#icon-mail"/></svg>hi@glimmernails.example</span><span class="contact__item"><svg class="icon"><use href="#icon-web"/></svg>www.glimmernailsalon.example</span></div>
    </footer>
  </section>

</main>
</body>
</html>
```